Beauty Clinic Treatment Menu (Lumen Nails & Beauty)

Needing a treatment menu designed for a beauty clinic in Whitianga, New Zealand. Like the colours grey, pink, white.
Elegant, Modern and feminine

Lumen Nails & Beauty
Dana Pirrett
Room1, 17 Corbel Street
Whitianga
0271836042
Dana.lumen@mailbay.example
lumenbeauty.example.nz

Target Market(s)

Females

Industry/Entity Type

Beauty Salon

Font styles to use
Serif

Colors

Designer to choose colors to be used in the design.

Requirements
Must have
• Chatterbook and Snapgrid logo

```html
<!DOCTYPE html>
<html lang="en">
<head>
<meta charset="utf-8">
<title>Lumen Nails &amp; Beauty – Treatment Menu</title>
<link href="https://fonts.googleapis.com/css2?family=Montserrat:ital,wght@0,500;0,600;1,500&family=Playfair+Display:wght@700&family=Quicksand:wght@400;500&family=Kaushan+Script&display=swap" rel="stylesheet">
<style>
:root{
  --pink:#e2418e;
  --pink-soft:#f29ac4;
  --grey:#dcdcdc;
  --yellow:#fce77c;
  --ink:#1f1f1f;
  --white:#ffffff;
  --plum:#7a2a78;
}
*{margin:0;padding:0;box-sizing:border-box}
html,body{width:1200px;height:309px;overflow:hidden;background:var(--white)}
.menu{position:relative;width:1200px;height:309px;overflow:hidden;font-family:"Quicksand",sans-serif;color:var(--ink)}
.panel{position:absolute;top:0;height:309px}
.panel--intro{left:0;width:133px;background:var(--pink)}
.panel--cover{left:133px;width:267px;background:var(--grey)}
.panel--story{left:400px;width:266px;background:var(--pink)}
.panel--nails{left:666px;width:134px;background:var(--yellow)}
.panel--facials{left:800px;width:135px;background:var(--yellow)}
.panel--eyes{left:935px;width:132px;background:var(--grey)}
.panel--body{left:1067px;width:133px;background:var(--pink)}
.abs{position:absolute}
.art{position:absolute;border-radius:4px}

.intro-text{left:0;top:17px;width:133px;text-align:center;color:var(--white);font-family:"Montserrat",sans-serif;font-style:italic;font-weight:500;font-size:7.3px;letter-spacing:2.1px;line-height:14.8px}

.brand-title{font-family:"Montserrat",sans-serif;font-weight:600;font-size:13px;letter-spacing:3.2px;line-height:20px}
.brand-title .pink{color:var(--pink)}
.brand-title .white{color:var(--white);padding-left:8px}

.wordmark{left:23px;top:132px;width:130px;text-align:center;font-family:"Playfair Display",serif;font-weight:700;font-size:13px;line-height:17px;color:var(--ink)}

.script{font-family:"Kaushan Script",cursive}
.get-in-touch{left:55px;top:238px;font-size:17px;color:#555}
.contact{left:20px;top:272px;width:170px;text-align:center;font-size:4.6px;line-height:6.8px;color:#333}

.story-title{left:32px;top:20px;font-size:16px;color:var(--white)}
.story-text{left:12px;top:54px;width:106px;text-align:center;color:var(--white);font-size:5.3px;line-height:7.85px}

.heading{font-family:"Montserrat",sans-serif;font-weight:600;letter-spacing:3px;font-size:17px;color:var(--pink)}
.heading--white{color:var(--white)}

.list{position:absolute;font-family:"Playfair Display",serif;font-weight:700;font-size:7.3px;line-height:10px}
.list .label{color:var(--pink);font-size:7px;letter-spacing:.4px;text-transform:uppercase;margin-top:11px}
.list .label:first-child{margin-top:0}
.list .desc{font-family:"Quicksand",sans-serif;font-weight:500;font-size:5.3px;line-height:9.3px}
.list .gap{margin-top:9px}
.list .bar{font-weight:400;padding:0 2px}

.facial{margin-bottom:9px}
.facial .desc{font-family:"Quicksand",sans-serif;font-weight:500;font-size:6px;line-height:9.8px}

.list--spaced div{margin-bottom:10.3px}
.list--body{color:var(--white)}
.list--body div{margin-bottom:10.8px}
</style>
</head>
<body>
<main class="menu">

  <section class="panel panel--intro">
    <p class="abs intro-text">ENJOY OUR CURATED<br>LIST OF SERVICES<br>ESPECIALLY MADE FOR<br>YOUR REQUIREMENTS</p>
    <div class="art" role="img" aria-label="Pattern of white dots" style="left:6px;top:245px;width:122px;height:58px;background:rgba(255,255,255,.22)"></div>
  </section>

  <section class="panel panel--cover">
    <div class="art" role="img" aria-label="Pattern of pink and white dots" style="left:33px;top:0;width:124px;height:72px;background:rgba(226,65,142,.25)"></div>
    <h1 class="abs brand-title" style="left:174px;top:12px"><span class="pink">BEAUTY</span><br><span class="white">CLINIC</span></h1>
    <p class="abs wordmark">Lumen<br>Nails &amp; Beauty</p>
    <div class="art" role="img" aria-label="Illustration of a dark-haired woman in a red floral top" style="left:160px;top:168px;width:100px;height:141px;background:linear-gradient(180deg,#3a3a3a 0%,#2a2a2a 45%,#d8343f 75%,#c92a35 100%);border-radius:40px 40px 0 0"></div>
    <p class="abs script get-in-touch">Get in touch</p>
    <p class="abs contact">Dana Pirrett, Room 1, 17 Corbel Street, Whitianga<br>0271-836-042<br>dana.lumen@mailbay.example<br>www.lumenbeauty.example.nz</p>
  </section>

  <section class="panel panel--story">
    <div class="art" role="img" aria-label="Illustration of colourful flowers and leaves" style="left:3px;top:0;width:118px;height:52px;background:linear-gradient(90deg,#7fd3c5,#b07ad6,#f07a4a,#9ccf6a);opacity:.55;border-radius:0 0 40px 40px"></div>
    <h2 class="abs script story-title">Our Story</h2>
    <p class="abs story-text">In 2014 I graduated from my Diploma in Beauty therapy at New Zealand's leading beauty school, Lumière. Since then I have worked at two amazing beauty salons, both which taught me valuable skills and information about beauty and nail therapies. I enjoy learning new skills and therapies, keeping up with the latest beauty trends, interacting with my clients and meeting new people. In early 2016 I made the decision to move to Whitianga to live with my partner, and I am loving the relaxed lifestyle!</p>
    <div class="art" role="img" aria-label="Illustration of an open purple cosmetics case" style="left:6px;top:171px;width:124px;height:124px;border-radius:50%;background:radial-gradient(circle at 50% 55%,var(--plum) 0%,#9b3a98 35%,var(--pink-soft) 36%,var(--pink-soft) 100%)"></div>
    <div class="art" role="img" aria-label="Pattern of white dots" style="left:140px;top:4px;width:122px;height:58px;background:rgba(255,255,255,.22)"></div>
    <div class="art" role="img" aria-label="Illustration of an eyeshadow palette and nail polish bottle" style="left:171px;top:115px;width:57px;height:78px;background:linear-gradient(135deg,#2a2a2a 0%,#3a2a30 60%,#e2418e 100%)"></div>
    <div class="art" role="img" aria-label="Pattern of yellow dots" style="left:140px;top:248px;width:122px;height:58px;background:rgba(252,231,124,.3)"></div>
  </section>

  <section class="panel panel--nails">
    <h2 class="abs heading" style="left:17px;top:16px">NAILS</h2>
    <div class="art" role="img" aria-label="Line drawing of a hand" style="left:87px;top:10px;width:45px;height:50px;background:rgba(31,31,31,.08)"></div>
    <div class="list" style="left:18px;top:61px">
      <div class="label">Manicure</div>
      <div>Gel Polish<span class="bar">|</span>$45</div>
      <div>Regular Polish<span class="bar">|</span>$40</div>
      <div class="label">Pedicure</div>
      <div>Gel Polish<span class="bar">|</span>$45</div>
      <div>Regular Polish<span class="bar">|</span>$40</div>
      <div class="label">Luxury Pedicure</div>
      <div class="desc">Includes: soak, exfoliation, heel rasping<br>and massage.</div>
      <div class="gap">Gel Polish<span class="bar">|</span>$60</div>
      <div>Regular Polish<span class="bar">|</span>$55</div>
      <div>Gel Removal &amp; Nail Tidy<span class="bar">|</span>$25</div>
      <div class="label">Add On</div>
      <div>Gel Removal<span class="bar">|</span>$5</div>
      <div>NTX<span class="bar">|</span>$5 per layer</div>
      <div>Builder Base<span class="bar">|</span>$10</div>
      <div>Nail Art/ Glitter<span class="bar">|</span>$POA</div>
    </div>
  </section>

  <section class="panel panel--facials">
    <h2 class="abs heading" style="left:12px;top:20px">FACIALS</h2>
    <div class="list" style="left:12px;top:59px;width:120px">
      <div class="facial"><div>Deep Cleansing Facial<span class="bar">|</span>$75</div><div class="desc">45 minutes Removes build up of dead skin cells, leaves the skin feeling soft and hydrated.</div></div>
      <div class="facial"><div>Therapeutic Facial<span class="bar">|</span>$105</div><div class="desc">60 minutes Tailored to suit your skins specific needs.</div></div>
      <div class="facial"><div>Rejuvenaiton Facial<span class="bar">|</span>$120</div><div class="desc">60 Minutes Active yet gentle treatment that facilitates dermal rejuvenation.</div></div>
      <div class="facial"><div>35% Glycolic Facial<span class="bar">|</span>$120</div><div class="desc">60 Minutes Hydrating, deep exfoliation treatment improving skin texture and appearance.</div></div>
      <div class="facial"><div>Dermaplaning<span class="bar">|</span>$120</div><div class="desc">Creates a smooth and radiant skin surface. Also removes<br>soft facial hairs.</div></div>
    </div>
    <div class="art" role="img" aria-label="Line drawing of a woman wearing a face mask" style="left:76px;top:236px;width:50px;height:68px;background:rgba(31,31,31,.1);border-radius:50% 50% 40% 40%"></div>
  </section>

  <section class="panel panel--eyes">
    <h2 class="abs heading" style="left:10px;top:20px">EYES</h2>
    <div class="art" role="img" aria-label="Line drawings of two closed eyes" style="left:70px;top:22px;width:55px;height:20px;background:rgba(31,31,31,.08)"></div>
    <div class="list list--spaced" style="left:11px;top:59px">
      <div>Velia Lash Lift<span class="bar">|</span>$115</div>
      <div>Eyebrow Shape<span class="bar">|</span>$19</div>
      <div>Eyebrow Tint<span class="bar">|</span>$18</div>
      <div>Eyelash Tint<span class="bar">|</span>$25</div>
      <div>Eye Trio<span class="bar">|</span>$45</div>
    </div>
    <h2 class="abs heading" style="left:10px;top:201px">FACE</h2>
    <div class="art" role="img" aria-label="Line drawing of a face in profile" style="left:70px;top:200px;width:55px;height:78px;background:rgba(31,31,31,.08)"></div>
    <div class="list list--spaced" style="left:10px;top:235px">
      <div>Lip<span class="bar">|</span>$15</div>
      <div>Chin<span class="bar">|</span>$19</div>
    </div>
  </section>

  <section class="panel panel--body">
    <h2 class="abs heading heading--white" style="left:12px;top:18px">BODY</h2>
    <div class="art" role="img" aria-label="Line drawing of a female figure" style="left:82px;top:42px;width:46px;height:124px;background:rgba(31,31,31,.08);border-radius:20px"></div>
    <div class="list list--body" style="left:12px;top:58px">
      <div>Under Arm | $20</div>
      <div>1/2 Leg | $35</div>
      <div>Full Leg<span class="bar">|</span>$55</div>
      <div>1/2 Arm<span class="bar">|</span>$30</div>
      <div>Full Arm<span class="bar">|</span>$40</div>
      <div>Bikini<span class="bar">|</span>$28</div>
      <div>Extended Bikini<span class="bar">|</span>$38</div>
      <div>Brazilian (1st Time)<span class="bar">|</span>$65</div>
      <div>Brazilian (4-6 Weeks)<span class="bar">|</span>$50</div>
      <div>Patches<span class="bar">|</span>$5</div>
    </div>
  </section>

</main>
</body>
</html>
```